Vela Habitat Real estate Costa del sol

we need a website for our Company based in Costa del sol, Spain. We sell properties on the spanish coast that is called costa del sol. We are concentrating on exclusive properties and would like the webdesign to show this. In our website we want to have area descriptions of the different areas we sell our Products. We will also implement a searchable database delivered by a third part where all properties for sale in Spain are listed. When looking into the designs we would like our main page to have a overview of the coast where the different areas are shown. Have a look at brightlomaview.com or ourtesa.com to see. The webpage will be presented in 4 languages, English, spanish, Swedish and norwegian, and shall of course also be prepared for social medias. We want an easy Contemporary design but still with an exclusive feeling!
Target Market(s)
Scandinavian and North european Citizens wants to buy a property in Spain
Industry/Entity Type
Real Estate
Number of Pages Required
5+ page
Look and feel

```html
<!DOCTYPE html>
<html lang="en">
<head>
<meta charset="utf-8">
<title>Vela Habitat – Real Estate Costa del Sol</title>
<link href="https://fonts.googleapis.com/css2?family=Open+Sans:wght@400;600;700&family=Playfair+Display:wght@400;700&display=swap" rel="stylesheet">
<style>
:root{
  --ink:#22242b;
  --ink-deep:#17181d;
  --panel:#2b2d34;
  --line:#e3e4e8;
  --muted:#8a8d96;
  --paper:#ffffff;
  --soft:#f4f5f7;
  --accent:#2d5fae;
  --gold:#c9a76a;
}
*{box-sizing:border-box;margin:0;padding:0}
html,body{width:1200px;height:2968px;overflow:hidden}
body{font-family:"Open Sans",Arial,sans-serif;color:var(--ink);background:var(--paper);font-size:13px}
.wrap{width:900px;margin:0 auto;position:relative}
.serif{font-family:"Playfair Display",Georgia,serif}

/* header */
.topbar{height:34px;background:var(--ink-deep);color:#c9cbd2;font-size:12px}
.topbar .wrap{display:flex;justify-content:flex-end;align-items:center;height:34px;gap:22px}
.lang{padding:2px 10px;border:1px solid #444;border-radius:2px}
.masthead{height:78px;border-bottom:1px solid var(--line)}
.masthead .wrap{display:flex;justify-content:space-between;align-items:center;height:78px}
.brand{display:flex;align-items:center;gap:10px;font-weight:700;font-size:20px;color:var(--ink)}
.brand-mark{width:30px;height:30px;border:3px solid var(--ink)}
.nav{display:flex;list-style:none}
.nav li{padding:0 16px;line-height:34px;font-size:13px;color:var(--ink)}
.nav li.active{background:var(--ink);color:#fff}

/* hero */
.hero{height:470px;position:relative;background:linear-gradient(180deg,#5f7a8f 0%,#7f8c7a 45%,#4d5a3d 80%,#2f3628 100%)}
.hero-caption{position:absolute;left:150px;top:150px;color:#fff}
.hero-caption .kicker{font-size:13px;letter-spacing:2px;text-transform:uppercase}
.hero-caption h1{font-family:"Playfair Display",Georgia,serif;font-size:32px;line-height:40px;margin-top:6px}
.btn-dark{display:inline-block;background:var(--ink);color:#fff;font-size:11px;padding:8px 16px;margin-top:16px}
.arrow{position:absolute;top:210px;width:30px;height:40px}
.arrow.left{left:60px}.arrow.right{right:60px}

/* search */
.search{height:278px;background:var(--panel);color:#fff;position:relative}
.tabs{position:absolute;top:-34px;left:150px;display:flex}
.tab{height:34px;line-height:34px;padding:0 24px;font-size:13px;color:#fff}
.tab.on{background:var(--panel)}
.tab.off{background:rgba(23,24,29,.75)}
.search .wrap{display:flex;padding-top:40px;gap:40px}
.discover{width:150px;text-transform:uppercase}
.discover small{font-size:12px;letter-spacing:1px;color:#c9cbd2}
.discover strong{display:block;font-family:"Playfair Display",Georgia,serif;font-weight:400;font-size:34px;line-height:40px;margin-top:4px}
.fields{flex:1;display:grid;grid-template-columns:repeat(3,1fr);gap:14px 18px;align-content:start}
.select{height:30px;background:#fff;color:#555;font-size:11px;padding:0 10px;display:flex;justify-content:space-between;align-items:center}
.range{font-size:11px;color:#c9cbd2}
.track{height:3px;background:#777;margin-top:10px;position:relative}
.track span{position:absolute;top:-5px;width:12px;height:12px;border-radius:50%;background:#fff}
.btn-search{height:30px;background:#fff;color:var(--ink);font-weight:600;font-size:12px;display:flex;align-items:center;justify-content:center;gap:8px;margin-top:8px}

/* section titles */
.title{display:flex;align-items:center;gap:12px;font-family:"Playfair Display",Georgia,serif;font-size:24px;text-transform:uppercase;letter-spacing:1px}
.title .mark{width:22px;height:22px;border:3px solid var(--ink)}
.title.center{justify-content:center}

/* developments */
.developments{height:470px;border-bottom:1px solid var(--line)}
.developments .wrap{padding-top:52px}
.dev-head{display:flex;justify-content:space-between;align-items:center;border-bottom:1px solid var(--line);padding-bottom:18px}
.view-all{background:var(--ink);color:#fff;font-size:11px;padding:6px 14px}
.dev-grid{display:grid;grid-template-columns:repeat(4,1fr);gap:16px;margin-top:28px}
.card{border:1px solid var(--line)}
.card .photo{height:150px}
.card .body{padding:10px 12px}
.card h3{font-size:12px;font-weight:700}
.card .meta{display:flex;justify-content:space-between;font-size:11px;color:var(--muted);margin-top:4px}
.card .stats{background:var(--ink);color:#fff;font-size:10px;display:flex;justify-content:space-around;height:28px;align-items:center}

/* promoted */
.promoted{height:590px;padding-top:60px}
.over{text-align:center;font-size:11px;color:var(--muted)}
.promo-grid{display:grid;grid-template-columns:440px 1fr 1fr;grid-template-rows:200px 190px;gap:10px;margin-top:32px}
.tile{position:relative;color:#fff}
.tile.big{grid-row:1 / 3}
.tile.wide{grid-column:2 / 4}
.tile .label{position:absolute;left:0;right:0;bottom:0;background:rgba(23,24,29,.82);display:flex;justify-content:space-between;align-items:center;padding:10px 14px}
.tile .label b{font-family:"Playfair Display",Georgia,serif;font-weight:400;font-size:15px}
.tile .label span{font-size:16px;font-weight:700}
.tile.wide .label{left:auto;right:0;top:40px;bottom:auto;background:none;flex-direction:column;align-items:flex-start}
.tile.wide .label b{font-size:22px}
.tile.wide .label span{font-size:26px}
.dots{display:flex;justify-content:center;gap:8px;margin-top:22px}
.dots i{width:8px;height:8px;border-radius:50%;background:#ccc}
.dots i:first-child{background:var(--ink)}

/* testimonials */
.testimonials{height:400px;background:linear-gradient(180deg,#23252c,#15161a);color:#fff}
.testimonials .wrap{padding-top:60px}
.testimonials .title .mark{border-color:#fff}
.t-body{display:flex;gap:40px;margin-top:46px;align-items:center}
.avatars{display:flex;flex-direction:column;gap:8px}
.avatar{width:44px;height:44px;background:linear-gradient(135deg,#8c8f97,#4a4d55)}
.quote{flex:1;border-left:1px solid #555;padding-left:40px;font-size:13px;line-height:22px;color:#d6d8de;text-align:center}
.quote cite{display:block;font-style:normal;font-weight:600;color:#fff;margin-top:14px;font-size:12px}

/* clients */
.clients{height:262px}
.clients .wrap{padding-top:48px;text-align:center}
.clients p{font-size:11px;color:var(--muted);margin:14px auto 0;width:620px;line-height:18px}
.client-row{display:grid;grid-template-columns:repeat(6,1fr);gap:12px;margin-top:30px}
.client{height:50px;border:1px solid var(--line);display:flex;align-items:center;justify-content:center;font-weight:700;font-size:14px;color:#3a3c44}

/* footer */
.footer{height:386px;background:var(--ink-deep);color:#b9bcc5;position:relative}
.footer .wrap{display:flex;padding-top:56px;gap:60px}
.f-about{width:250px;font-size:11px;line-height:18px}
.f-about .brand-mark{border-color:#fff;width:34px;height:34px;margin-bottom:16px}
.social{display:flex;gap:6px;margin-top:18px}
.social i{width:22px;height:22px;background:#3a3c44}
.social i:nth-child(4){background:#fff}
.footer h4{font-family:"Playfair Display",Georgia,serif;font-weight:400;font-size:18px;color:#fff;margin-bottom:18px}
.contact{width:220px;font-size:11px;line-height:18px}
.contact .row{display:flex;gap:8px;margin-bottom:10px}
.contact .row b{color:#fff}
.cities ul{list-style:none;columns:2;column-gap:50px;font-size:11px;line-height:22px}
.cities li::before{content:"› ";color:var(--gold)}
.bottom{position:absolute;left:0;right:0;bottom:0;height:44px;background:#111216;font-size:11px}
.bottom .wrap{display:flex;justify-content:space-between;align-items:center;height:44px;padding:0}
.bottom nav{display:flex;gap:20px}
</style>
</head>
<body>

<header>
  <div class="topbar"><div class="wrap">
    <span class="lang">English ▾</span>
    <span>Call: (0100) 555 210</span>
  </div></div>
  <div class="masthead"><div class="wrap">
    <div class="brand"><span class="brand-mark"></span>Vela Habitat</div>
    <ul class="nav">
      <li class="active">Home</li><li>About Us</li><li>Costa del Sol</li><li>Service</li><li>Testimonials</li><li>Contact Us</li>
    </ul>
  </div></div>
</header>

<section class="hero" role="img" aria-label="Photograph of a large stone villa with gardens at dusk">
  <svg class="arrow left" viewBox="0 0 30 40"><path d="M22 4 6 20l16 16" fill="none" stroke="#fff" stroke-width="3"/></svg>
  <svg class="arrow right" viewBox="0 0 30 40"><path d="m8 4 16 16L8 36" fill="none" stroke="#fff" stroke-width="3"/></svg>
  <div class="hero-caption">
    <div class="kicker">We Are Always Here To</div>
    <h1>We Are Always Here To<br>Fulfill Your Dreams</h1>
    <span class="btn-dark">Read More</span>
  </div>
</section>

<section class="search">
  <div class="tabs">
    <div class="tab on">⌂ Find Your Home</div>
    <div class="tab off">⌂ House for sell</div>
  </div>
  <div class="wrap">
    <div class="discover"><small>Discover Your</small><strong>Dream House</strong></div>
    <div class="fields">
      <div class="select">Location <span>▾</span></div>
      <div class="select">Sub Location <span>▾</span></div>
      <div class="select">Status <span>▾</span></div>
      <div class="select">No of Bedrooms <span>▾</span></div>
      <div class="select">No of Bathrooms <span>▾</span></div>
      <div class="select">Property Type <span>▾</span></div>
      <div class="range">Size of Area<div class="track"><span style="left:0"></span><span style="left:70%"></span></div></div>
      <div class="range">Price (€)<div class="track"><span style="left:10%"></span><span style="left:80%"></span></div></div>
      <div class="btn-search"><svg width="12" height="12" viewBox="0 0 12 12"><circle cx="5" cy="5" r="3.5" fill="none" stroke="#22242b" stroke-width="1.6"/><path d="m7.5 7.5 3.5 3.5" stroke="#22242b" stroke-width="1.6"/></svg>Search Property</div>
    </div>
  </div>
</section>

<section class="developments"><div class="wrap">
  <div class="dev-head"><h2 class="title"><span class="mark"></span>New Developments</h2><span class="view-all">View All</span></div>
  <div class="dev-grid">
    <article class="card"><div class="photo" role="img" aria-label="Photograph of a modern villa at twilight" style="background:linear-gradient(180deg,#4b5b78,#2c2f3a)"></div>
      <div class="body"><h3>El Rehab Mountain Villa</h3><div class="meta"><span>€ 152,000</span><span>Marbella, ES</span></div></div>
      <div class="stats"><span>▭ 3 Beds</span><span>◫ 2 Baths</span><span>▢ 240 m²</span></div></article>
    <article class="card"><div class="photo" role="img" aria-label="Photograph of a contemporary house at night" style="background:linear-gradient(180deg,#3a3f4c,#1f2128)"></div>
      <div class="body"><h3>El Rehab Mountain Villa</h3><div class="meta"><span>€ 152,000</span><span>Marbella, ES</span></div></div>
      <div class="stats"><span>▭ 3 Beds</span><span>◫ 2 Baths</span><span>▢ 240 m²</span></div></article>
    <article class="card"><div class="photo" role="img" aria-label="Photograph of a family home under a blue sky" style="background:linear-gradient(180deg,#7fa3c9,#9a8a6e)"></div>
      <div class="body"><h3>El Rehab Mountain Villa</h3><div class="meta"><span>€ 152,000</span><span>Marbella, ES</span></div></div>
      <div class="stats"><span>▭ 3 Beds</span><span>◫ 2 Baths</span><span>▢ 240 m²</span></div></article>
    <article class="card"><div class="photo" role="img" aria-label="Photograph of a lit villa in the evening" style="background:linear-gradient(180deg,#5a6a8a,#6b5a45)"></div>
      <div class="body"><h3>El Rehab Mountain Villa</h3><div class="meta"><span>€ 152,000</span><span>Marbella, ES</span></div></div>
      <div class="stats"><span>▭ 3 Beds</span><span>◫ 2 Baths</span><span>▢ 240 m²</span></div></article>
  </div>
</div></section>

<section class="promoted"><div class="wrap">
  <div class="over">Best Property in Villa City</div>
  <h2 class="title center" style="margin-top:6px"><span class="mark"></span>Specially Promoted</h2>
  <div class="promo-grid">
    <div class="tile big" role="img" aria-label="Photograph of a luxury villa with a lawn at sunset" style="background:linear-gradient(180deg,#7c6e9a,#b58a7a 55%,#4c5a3a)">
      <div class="label"><b>Luxury Villa</b><span>€152,000</span></div></div>
    <div class="tile wide" role="img" aria-label="Photograph of a villa with a lit swimming pool at night" style="background:linear-gradient(135deg,#2a3f5e,#16202e 60%,#3b6d86)">
      <div class="label"><b>Swimming Pool</b><small>3d Properties</small><span>€147,000</span></div></div>
    <div class="tile" role="img" aria-label="Photograph of a cozy house with a garden" style="background:linear-gradient(180deg,#8aa0b8,#5e6b4f)">
      <div class="label"><b>Cozy house</b><span>€152,000</span></div></div>
    <div class="tile" role="img" aria-label="Photograph of a house with a front garden" style="background:linear-gradient(180deg,#6e7f96,#4a5540)">
      <div class="label"><b>Garden</b><span>€152,000</span></div></div>
  </div>
  <div class="dots"><i></i><i></i><i></i><i></i></div>
</div></section>

<section class="testimonials" role="img" aria-label="Darkened photograph of a villa interior behind client testimonials"><div class="wrap">
  <h2 class="title center"><span class="mark"></span>Clients Testimonials</h2>
  <div class="t-body">
    <div class="avatars">
      <div class="avatar" role="img" aria-label="Client portrait"></div>
      <div class="avatar" role="img" aria-label="Client portrait"></div>
      <div class="avatar" role="img" aria-label="Client portrait"></div>
    </div>
    <blockquote class="quote">We searched along the coast for months before we found the team. They listened to what we wanted, showed us only homes that matched, and guided us through every step of the purchase in our own language. Today we enjoy our terrace above the sea, and we would recommend them to every family from the north who dreams of the sun.
      <cite>Mr. Erik Nilsen, Company Name</cite></blockquote>
  </div>
</div></section>

<section class="clients"><div class="wrap">
  <h2 class="title center"><span class="mark"></span>Our Valued Clients</h2>
  <p>Trusted by partners across the coast who share our care for quality homes, clear advice and lasting relationships with every buyer we serve.</p>
  <div class="client-row">
    <div class="client">Holvik</div><div class="client">Linea Works</div><div class="client">Brisa Group</div>
    <div class="client">Olmo Books</div><div class="client">Arqa</div><div class="client">Tidefield</div>
  </div>
</div></section>

<footer class="footer">
  <div class="wrap">
    <div class="f-about">
      <div class="brand-mark"></div>
      <p>Exclusive homes on the Costa del Sol for buyers from Scandinavia and northern Europe. Personal service from first viewing to the keys in your hand.</p>
      <div class="social"><i></i><i></i><i></i><i></i><i></i></div>
    </div>
    <div class="contact">
      <h4>Get In Touch</h4>
      <div class="row"><svg width="12" height="14" viewBox="0 0 12 14"><path d="M6 1a4 4 0 0 1 4 4c0 3-4 8-4 8S2 8 2 5a4 4 0 0 1 4-4z" fill="#c9a76a"/></svg><div><b>Vela Habitat</b><br>Avenida del Mar 12<br>Marbella, Spain</div></div>
      <div class="row"><svg width="12" height="12" viewBox="0 0 12 12"><path d="M2 1h3l1 3-2 1a7 7 0 0 0 3 3l1-2 3 1v3a1 1 0 0 1-1 1A10 10 0 0 1 1 2a1 1 0 0 1 1-1z" fill="#c9a76a"/></svg>(0100) 555 210</div>
      <div class="row"><svg width="12" height="10" viewBox="0 0 12 10"><rect x=".5" y=".5" width="11" height="9" fill="none" stroke="#c9a76a"/><path d="m.5.5 5.5 5 5.5-5" fill="none" stroke="#c9a76a"/></svg>info@velahabitat.com</div>
    </div>
    <div class="cities">
      <h4>Property Cities</h4>
      <ul><li>Alaska</li><li>California</li><li>Colorado</li><li>Florida</li><li>Hawaii</li><li>Louisiana</li><li>Michigan</li><li>Mississippi</li><li>New Jersey</li><li>New York</li><li>Oklahoma</li><li>Texas</li><li>Washington</li><li>Wisconsin</li></ul>
    </div>
  </div>
  <div class="bottom"><div class="wrap">
    <span>© Copyright 2016. Vela Habitat. All Right Reserved.</span>
    <nav><span>Home</span><span>About Us</span><span>Costa del Sol</span><span>Service</span><span>Testimonials</span><span>Contact Us</span></nav>
  </div></div>
</footer>

</body>
</html>
```